Zielgruppe
Verkauf und Einbau von Fenstern, Haustüren, Rollläden, Raffstore, Markisen, Insektenschutzgitter, Plissees
Aufgabenstellung
Es soll das gleiche Farbschema meines Firmenlogos haben. Grauer Hintergrund, kleine gelbe Akzente und schwarze Schrift

```html
<!DOCTYPE html>
<html lang="de">
<head>
<meta charset="utf-8">
<title>Sorvik – Verkauf und Einbau</title>
<link href="https://fonts.googleapis.com/css2?family=Comfortaa:wght@400;600&family=Open+Sans:wght@300;400;600;700&display=swap" rel="stylesheet">
<style>
:root{
  --yellow:#ffc000;
  --grey:#8e8e8e;
  --grey-dark:#6f6f6f;
  --ink:#222;
  --text:#555;
  --white:#fff;
}
*{box-sizing:border-box;margin:0;padding:0}
html,body{width:1200px;height:4511px;overflow:hidden;background:var(--white)}
body{position:relative;font-family:"Open Sans",sans-serif;color:var(--ink)}
.abs{position:absolute}
.band{position:absolute;left:0;width:1200px}
.display{font-family:"Comfortaa",sans-serif;font-weight:400}
p.copy{font-size:9.5px;line-height:18px;color:var(--text);font-weight:300;margin-bottom:14px}
.on-grey p.copy{color:#f0f0f0}
.btn{position:absolute;display:flex;align-items:center;justify-content:center;font-size:14px;letter-spacing:.8px;color:#444;background:var(--white);border:1px solid #bbb}
.btn.yellow{background:var(--yellow);color:var(--white);border:none}
.photo{position:absolute}

.header{top:0;height:109px;background:var(--yellow)}
.brand{position:absolute;left:0;width:1200px;top:12px;text-align:center;color:var(--white)}
.brand .mark{display:inline-block;width:36px;height:36px;border:2px solid var(--white);border-radius:50%}
.brand .name{font-family:"Comfortaa",sans-serif;font-size:14px;letter-spacing:1px;margin-top:4px}
.brand .tag{font-family:"Comfortaa",sans-serif;font-size:6px;letter-spacing:.6px;margin-top:2px}
.contact-icons{position:absolute;left:998px;top:18px;display:flex;flex-direction:column;gap:8px}
.nav{top:109px;height:35px;display:flex;align-items:center;justify-content:center;gap:6px;font-family:"Comfortaa",sans-serif;font-size:9px;letter-spacing:.5px}
.nav .dot{color:var(--yellow)}

.hero{top:144px;height:501px;background:linear-gradient(100deg,#4e6b3a 0%,#5c6460 18%,#7d838a 45%,#bfc4c6 70%,#dfe3e2 100%)}
.hero-title{position:absolute;top:372px;left:0;width:1200px;text-align:center;font-family:"Open Sans",sans-serif;font-weight:600;font-size:52px;letter-spacing:2px;color:var(--white)}
.hero-btn{position:absolute;left:477px;top:461px;width:241px;height:61px;background:var(--white);display:flex;align-items:center;justify-content:center;font-family:"Comfortaa",sans-serif;font-size:27px;letter-spacing:2px;color:#222}
.arrow{position:absolute;width:96px;height:87px;background:rgba(255,255,255,.35);display:flex;align-items:center;justify-content:center}

.section-title{position:absolute;left:0;width:1200px;text-align:center;font-size:20px}
.center-copy{position:absolute;left:280px;width:640px;text-align:center}

.tiles{position:absolute;top:1011px;height:249px;background:var(--grey)}
.tile{position:absolute;width:125px;height:125px;display:flex;flex-direction:column;align-items:center;justify-content:center;gap:8px;color:var(--white);font-size:9.5px;letter-spacing:.6px;text-align:center}
.tile.active{background:var(--white);color:#999}

.col h2{font-size:20px;line-height:30px;margin-bottom:18px}
.col ul{list-style:none;font-size:9px;line-height:19px;color:var(--text)}
.col ul li::before{content:"■ ";color:var(--yellow);font-size:6px}
.col strong{display:block;font-size:9.5px;margin-bottom:2px}
.partners{position:absolute;top:1585px;left:189px;display:flex;align-items:center;gap:50px}
.partners span{font-family:"Open Sans",sans-serif;font-weight:600;font-size:30px;color:#333}

.grey{background:var(--grey)}
.on-grey h2{color:var(--white)}
.dots{position:absolute;left:330px;top:2115px;display:flex;gap:10px}
.dots i{width:14px;height:14px;border-radius:50%;background:var(--white)}
.dots i.off{background:#999}

.footer{position:absolute;top:4480px;left:0;width:1200px;text-align:center;font-family:"Comfortaa",sans-serif;font-size:9px;letter-spacing:.5px}
.footer .dot{color:var(--yellow)}
</style>
</head>
<body>

<header class="band header">
  <div class="brand">
    <span class="mark"></span>
    <div class="name">SORVIK</div>
    <div class="tag">FENSTER · TÜREN · MONTAGE</div>
  </div>
  <div class="contact-icons">
    <svg width="20" height="18" viewBox="0 0 20 18" fill="none" stroke="#fff" stroke-width="1.4"><path d="M4 2l3 3-2 2c1 3 3 5 6 6l2-2 3 3-2 2C8 16 2 10 2 4z"/></svg>
    <svg width="20" height="16" viewBox="0 0 20 16" fill="none" stroke="#fff" stroke-width="1.4"><rect x="1" y="2" width="18" height="12"/><path d="M1 2l9 7 9-7"/></svg>
    <svg width="20" height="20" viewBox="0 0 20 20" fill="none" stroke="#fff" stroke-width="1.4"><circle cx="10" cy="10" r="8"/><path d="M10 5v5l3 2"/></svg>
  </div>
</header>

<nav class="band nav">
  <span>PRODUKTE</span><span class="dot">●</span><span>PROJEKTE</span><span class="dot">●</span><span>DAS SIND WIR</span><span class="dot">●</span><span>KONTAKT</span>
</nav>

<section class="band hero" role="img" aria-label="Foto einer modernen grauen Haustür mit Glasfeld und Pflanzen davor">
  <div class="arrow" style="left:0;top:189px"><svg width="34" height="40" viewBox="0 0 34 40"><path d="M24 4L8 20l16 16" fill="none" stroke="#fff" stroke-width="7"/></svg></div>
  <div class="arrow" style="left:1104px;top:189px"><svg width="34" height="40" viewBox="0 0 34 40"><path d="M10 4l16 16-16 16" fill="none" stroke="#fff" stroke-width="7"/></svg></div>
</section>
<div class="hero-title">VERKAUF UND EINBAU</div>
<div class="hero-btn">HAUSTÜREN</div>

<h1 class="section-title display" style="top:716px">Headline</h1>
<div class="center-copy" style="top:762px">
  <p class="copy">Lorem ipsum dolor sit amet, consectetuer adipiscing elit. Aenean commodo ligula eget dolor. Aenean massa. Cum sociis natoque penatibus et magnis dis parturient montes, nascetur ridiculus mus. Donec quam felis, ultricies nec, pellentesque eu, pretium quis, sem.</p>
  <p class="copy">Nulla consequat massa quis enim. Donec pede justo, fringilla vel, aliquet nec, vulputate eget, arcu. In enim justo, rhoncus ut, imperdiet a, venenatis vitae, justo. Nullam dictum felis eu pede mollis pretium. Integer tincidunt. Cras dapibus. Vivamus elementum semper nisi. Aenean vulputate eleifend tellus. Aenean leo ligula, porttitor eu, consequat vitae, eleifend ac, enim. Aliquam lorem ante, dapibus in, viverra quis, feugiat a.</p>
</div>
<div class="btn" style="left:505px;top:906px;width:177px;height:45px">ANFRAGE STELLEN</div>

<section class="band tiles">
  <div class="tile active" style="left:163px;top:0">
    <svg width="34" height="56" viewBox="0 0 34 56" fill="none" stroke="#999" stroke-width="2"><rect x="3" y="2" width="28" height="52"/><rect x="9" y="8" width="7" height="20"/><rect x="18" y="8" width="7" height="20"/><rect x="9" y="32" width="16" height="16"/></svg>HAUSTÜREN</div>
  <div class="photo" role="img" aria-label="Foto eines geöffneten Fensters mit Pflanzen" style="left:288px;top:0;width:125px;height:125px;background:linear-gradient(135deg,#5d7a3c,#c9ccc8)"></div>
  <div class="tile" style="left:413px;top:0">
    <svg width="52" height="52" viewBox="0 0 52 52" fill="none" stroke="#fff" stroke-width="2"><rect x="6" y="4" width="40" height="8"/><path d="M10 12v36h32V12M10 20h32M10 28h32M10 36h32M10 44h32"/></svg>ROLLADEN</div>
  <div class="photo" role="img" aria-label="Foto von Lamellen eines Raffstores" style="left:538px;top:0;width:125px;height:125px;background:linear-gradient(160deg,#3f3f3f,#8a8a8a,#4a4a4a)"></div>
  <div class="tile" style="left:663px;top:0">
    <svg width="52" height="52" viewBox="0 0 52 52" fill="none" stroke="#fff" stroke-width="2"><rect x="4" y="4" width="44" height="44"/><path d="M12 10v32M18 10v32M24 10v32M30 10v32M36 10v32M42 10v32M10 12h32M10 18h32M10 24h32M10 30h32M10 36h32"/></svg>INSEKTEN<br>SCHUTZGITTER</div>
  <div class="photo" role="img" aria-label="Foto eines beigen Plissees im Licht" style="left:788px;top:0;width:125px;height:125px;background:linear-gradient(150deg,#f2d2b0,#e3a27a)"></div>
  <div class="tile" style="left:913px;top:0">
    <svg width="60" height="52" viewBox="0 0 60 52" fill="none" stroke="#fff" stroke-width="2"><path d="M4 6h52M6 6l-2 12h52l-2-12M8 18v30h44V18M16 24h28v24H16z"/></svg>MARKISE</div>

  <div class="photo" role="img" aria-label="Foto einer Hausfront mit dunkler Haustür" style="left:163px;top:125px;width:125px;height:124px;background:linear-gradient(90deg,#2f2f2f,#d9d9d9)"></div>
  <div class="tile" style="left:288px;top:125px">
    <svg width="48" height="52" viewBox="0 0 48 52" fill="none" stroke="#fff" stroke-width="2"><rect x="4" y="2" width="40" height="48"/><path d="M4 14h40M24 14v36M10 22l8 8M30 22l8 8"/></svg>FENSTER</div>
  <div class="photo" role="img" aria-label="Foto einer Fensterfront mit Rollladen" style="left:413px;top:125px;width:125px;height:124px;background:linear-gradient(180deg,#707070,#2d2d2d)"></div>
  <div class="tile" style="left:538px;top:125px">
    <svg width="52" height="52" viewBox="0 0 52 52" fill="none" stroke="#fff" stroke-width="2"><rect x="6" y="2" width="40" height="6"/><path d="M8 12h36M8 18h36M8 24h36M8 30h36M8 36h36M8 42h36M8 48h36"/></svg>RAFFSTORE</div>
  <div class="photo" role="img" aria-label="Foto eines Plissees am Fenster" style="left:663px;top:125px;width:125px;height:124px;background:linear-gradient(90deg,#e8d6c6,#c8b7ad,#9a8f8a)"></div>
  <div class="tile" style="left:788px;top:125px">
    <svg width="48" height="52" viewBox="0 0 48 52" fill="none" stroke="#fff" stroke-width="2"><path d="M6 4h36M6 4l4 6-4 6 4 6-4 6 4 6-4 6 4 6M42 4l-4 6 4 6-4 6 4 6-4 6 4 6-4 6M8 10h32M8 16h32M8 22h32M8 28h32M8 34h32M8 40h32"/></svg>PLISSEES</div>
  <div class="photo" role="img" aria-label="Foto einer Markise vor blauem Himmel" style="left:913px;top:125px;width:124px;height:124px;background:linear-gradient(160deg,#7fa9d8,#d8dde2,#a9a9a9)"></div>
</section>

<section class="col abs" style="left:189px;top:1316px;width:380px">
  <h2 class="display">Wir nutzen Qualtiätprodukte</h2>
  <p class="copy">Lorem ipsum dolor sit amet, consectetuer adipiscing elit. Aenean commodo ligula eget dolor. Aenean massa. Cum sociis natoque penatibus et magnis dis parturient montes, nascetur ridiculus mus. Donec quam felis, ultricies nec, pellentesque eu, pretium quis, sem.</p>
  <p class="copy">Nulla consequat massa quis enim. Donec pede justo, fringilla vel, aliquet nec, vulputate eget, arcu. In enim justo, rhoncus ut, imperdiet a, venenatis vitae, justo. Nullam dictum felis eu pede mollis pretium. Integer tincidunt. Cras dapibus. Vivamus elementum semper nisi. Aenean vulputate eleifend tellus. Aenean leo ligula, porttitor eu, consequat vitae, eleifend ac, enim. Aliquam lorem ante, dapibus in, viverra quis, feugiat a.</p>
</section>
<div class="partners"><span>Fenra</span><span style="font-size:18px">Solmo</span><span>Tarvo</span></div>

<section class="col abs" style="left:641px;top:1316px;width:380px">
  <h2 class="display">Kompetene Beratung, Verkauf und Einbau</h2>
  <p class="copy">Lorem ipsum dolor sit amet, consectetuer adipiscing elit. Aenean commodo ligula eget dolor. Aenean massa. Cum sociis natoque penatibus et magnis dis parturient montes, nascetur ridiculus mus. Donec quam felis, ultricies nec, pellentesque eu, pretium quis, sem.</p>
  <strong>Verkauf und Einbau</strong>
  <ul><li>Haustüren</li><li>Fenster und Rolladen</li><li>Markisen</li><li>Insektenschutzgitter</li><li>Faltstore</li><li>Plissees</li></ul>
</section>
<div class="btn" style="left:461px;top:1677px;width:264px;height:45px">JETZT KONTAKT AUFNEHMEN</div>

<section class="band grey on-grey" style="top:1775px;height:504px">
  <div class="photo" role="img" aria-label="Foto einer anthrazitfarbenen Haustür an einer hellen Fassade" style="left:163px;top:68px;width:448px;height:300px;background:linear-gradient(90deg,#4e6a36 0%,#6f7473 20%,#3a3d40 40%,#b8bdbf 70%,#6f8a3f 100%)"></div>
  <div class="arrow" style="left:163px;top:175px;width:60px;height:80px"><svg width="26" height="36" viewBox="0 0 26 36"><path d="M20 3L6 18l14 15" fill="none" stroke="#fff" stroke-width="6"/></svg></div>
  <div class="arrow" style="left:551px;top:175px;width:60px;height:80px"><svg width="26" height="36" viewBox="0 0 26 36"><path d="M6 3l14 15-14 15" fill="none" stroke="#fff" stroke-width="6"/></svg></div>
  <div class="col abs" style="left:648px;top:92px;width:380px">
    <h2 class="display">Haustüren und Fenster: Ganz nach Ihren Wünschen</h2>
    <p class="copy">Lorem ipsum dolor sit amet, consectetuer adipiscing elit. Aenean commodo ligula eget dolor. Aenean massa. Cum sociis natoque penatibus et magnis dis parturient montes, nascetur ridiculus mus. Donec quam felis, ultricies nec, pellentesque eu, pretium quis, sem.</p>
    <p class="copy">Nulla consequat massa quis enim. Donec pede justo, fringilla vel, aliquet nec, vulputate eget, arcu. In enim justo, rhoncus ut, imperdiet a, venenatis vitae, justo. Nullam dictum felis eu pede mollis pretium. Integer tincidunt. Cras dapibus. Vivamus elementum semper nisi. Aenean vulputate eleifend tellus. Aenean leo ligula, porttitor eu, consequat vitae, eleifend ac, enim. Aliquam lorem ante, dapibus in, viverra quis, feugiat a.</p>
  </div>
  <div class="btn yellow" style="left:447px;top:418px;width:292px;height:44px">BERATUNGSTERMIN VEREINBAREN</div>
</section>
<div class="dots"><i></i><i></i><i class="off"></i><i></i><i></i></div>

<h2 class="section-title display" style="top:2346px">Blick -und Sonnenschutz mit Raffstore und Plissee</h2>
<div class="center-copy" style="top:2390px">
  <p class="copy">Lorem ipsum dolor sit amet, consectetuer adipiscing elit. Aenean commodo ligula eget dolor. Aenean massa. Cum sociis natoque penatibus et magnis dis parturient montes, nascetur ridiculus mus. Donec quam felis, ultricies nec, pellentesque eu, pretium quis, sem.</p>
  <p class="copy">Nulla consequat massa quis enim. Donec pede justo, fringilla vel, aliquet nec, vulputate eget, arcu. In enim justo, rhoncus ut, imperdiet a, venenatis vitae, justo. Nullam dictum felis eu pede mollis pretium. Integer tincidunt. Cras dapibus. Vivamus elementum semper nisi. Aenean vulputate eleifend tellus. Aenean leo ligula, porttitor eu, consequat vitae, eleifend ac, enim. Aliquam lorem ante, dapibus in, viverra quis, feugiat a.</p>
</div>
<div class="photo" role="img" aria-label="Foto von Händen, die Plissee-Stoffmuster und Farbfächer auswählen" style="left:277px;top:2540px;width:623px;height:417px;background:linear-gradient(150deg,#c79a7a 0%,#e9e6e2 35%,#f3f1ee 55%,#9a9690 80%,#4a4846 100%)"></div>

<section class="band grey on-grey" style="top:3048px;height:894px">
  <div class="col abs" style="left:187px;top:88px;width:390px">
    <h2 class="display">Markisen in verschiedenen Qualitäten, Ausführungen und Größen</h2>
    <p class="copy">Lorem ipsum dolor sit amet, consectetuer adipiscing elit. Aenean commodo ligula eget dolor. Aenean massa. Cum sociis natoque penatibus et magnis dis parturient montes, nascetur ridiculus mus. Donec quam felis, ultricies nec, pellentesque eu, pretium quis, sem.</p>
    <p class="copy">Nulla consequat massa quis enim. Donec pede justo, fringilla vel, aliquet nec, vulputate eget, arcu. In enim justo, rhoncus ut, imperdiet a, venenatis vitae, justo. Nullam dictum felis eu pede mollis pretium. Integer tincidunt. Cras dapibus. Vivamus elementum semper nisi. Aenean vulputate eleifend tellus. Aenean leo ligula, porttitor eu, consequat vitae, eleifend ac, enim. Aliquam lorem ante, dapibus in, viverra quis, feugiat a.</p>
  </div>
  <div class="col abs" style="left:631px;top:85px;width:390px">
    <h2 class="display">Insektenschutzgitter:<br>Insenkten sind wichtig, deshalb sollten sie draußen bleiben</h2>
    <p class="copy">Lorem ipsum dolor sit amet, consectetuer adipiscing elit. Aenean commodo ligula eget dolor. Aenean massa. Cum sociis natoque penatibus et magnis dis parturient montes, nascetur ridiculus mus. Donec quam felis, ultricies nec, pellentesque eu, pretium quis, sem.</p>
    <p class="copy">Nulla consequat massa quis enim. Donec pede justo, fringilla vel, aliquet nec, vulputate eget, arcu. In enim justo, rhoncus ut, imperdiet a, venenatis vitae, justo. Nullam dictum felis eu pede mollis pretium. Integer tincidunt. Cras dapibus. Vivamus elementum semper nisi. Aenean vulputate eleifend tellus. Aenean leo ligula, porttitor eu, consequat vitae, eleifend ac, enim. Aliquam lorem ante, dapibus in, viverra quis, feugiat a.</p>
  </div>
  <div class="photo" role="img" aria-label="Foto von braun-beige gestreiften Markisenstoffen" style="left:165px;top:438px;width:218px;height:228px;background:linear-gradient(135deg,#e8cdb5,#7a5646,#e6c7ad,#5e4236)"></div>
  <div class="photo" role="img" aria-label="Foto einer Terrasse mit ausgefahrener Markise" style="left:383px;top:438px;width:437px;height:228px;background:linear-gradient(180deg,#8fb3d9 0%,#d9d6cf 40%,#b78d62 75%,#7d7a63 100%)"></div>
  <div class="photo" role="img" aria-label="Foto einer Rolle Insektenschutzgewebe" style="left:820px;top:438px;width:215px;height:228px;background:linear-gradient(135deg,#cfd2d4,#8a8d90,#bfc2c4)"></div>
  <div class="btn" style="left:470px;top:722px;width:292px;height:44px">BERATUNGSTERMIN VEREINBAREN</div>
</section>

<h2 class="section-title display" style="top:4010px">Projekteinblicke</h2>
<div class="photo" role="img" aria-label="Foto von Monteuren auf Leitern beim Einbau eines Rollladens an einem weißen Haus" style="left:163px;top:4059px;width:874px;height:377px;background:linear-gradient(180deg,#eeeeee 0%,#d7d7d7 55%,#b3a38d 100%)">
  <div class="arrow" style="left:0;top:145px;width:66px;height:88px"><svg width="28" height="38" viewBox="0 0 28 38"><path d="M22 3L6 19l16 16" fill="none" stroke="#fff" stroke-width="6"/></svg></div>
  <div class="arrow" style="left:808px;top:145px;width:66px;height:88px"><svg width="28" height="38" viewBox="0 0 28 38"><path d="M6 3l16 16-16 16" fill="none" stroke="#fff" stroke-width="6"/></svg></div>
</div>

<footer class="footer">KONTAKT <span class="dot">●</span> IMPRESSUM <span class="dot">●</span> SITEMAP</footer>

</body>
</html>
```